Create a pouch design for a new sports supplement product

Dimensions are 235mm (width) x 335mm (length) x 110mm (gusset)
File 1 - Extension of design brief please read both briefs
File 2 - Is 2 potential pouches this is just to give you a better example of size the dimensions are for the pouch on the right. This picture is not to give you design ideas as I am not very keen on either of these designs.
We need a design to be printed onto the pouches of our whey protein product. The brand name is 'Stellar Fuelworks' and needs to be displayed on the packaging either just writing or a simple logo design. I am not the most creative person in the world but have put together a more detailed brief listing some of the key information that needs to be included on the pouch (See attachment) Please feel free if you have experience of this the sports supplement market or have different ideas then please feel free to explore them.
The pouch would either be printed straight onto the pouch, or possibly just a printed label (front & back) to be stuck onto the pouch. Please design either or both.
Open to different colour schemes. Design has to be modern looking and eye-catching.
Some key points;
High quality whey protein concentrate
All Natural
Soy free
Great tasting
Please google image search 'protein pouches' to see other designs if your not familiar with the sports supplement market.
Any questions feel free to ask.
Updates
Hi, Thanks for all your design! I am really busy at the moment so haven't had chance to give feedback and have a proper look through all the designs. I have extended the time frame to give myself chance to give proper feedback and see any changes needed. Expect feedback sunday at the latest, and I will be pick a design early next week.
Target Market(s)
Sports supplement market. Product is a whey protein shake
Industry/Entity Type
Nutrition
Look and feel
Each slider illustrates characteristics of the customer's brand and the style your logo design should communicate.

```html
<!DOCTYPE html>
<html lang="en">
<head>
<meta charset="utf-8">
<title>Stellar Fuelworks – Natural Whey Protein Pouch</title>
<link href="https://fonts.googleapis.com/css2?family=Exo+2:ital,wght@0,300;0,400;0,600;0,700;1,800;1,900&family=Orbitron:wght@500;700&display=swap" rel="stylesheet">
<style>
  :root{
    --bg:#4a4a4a;
    --pouch-dark:#101018;
    --silver-light:#f2f2f4;
    --silver-mid:#c9cacd;
    --silver-dark:#8c8d92;
    --cyan:#4fd3e6;
    --cyan-deep:#1a8ea8;
    --pink:#e45bc6;
    --crimson:#9b1f3c;
    --teal-text:#2c7f88;
    --brand:#bfeef5;
  }
  *{margin:0;padding:0;box-sizing:border-box}
  html,body{width:1200px;height:1197px;overflow:hidden;background:var(--bg)}
  .canvas{position:relative;width:1200px;height:1197px;background:var(--bg);font-family:"Exo 2",sans-serif}
  .pouch{position:absolute;left:333px;top:197px;width:512px;height:808px;overflow:hidden;border-radius:6px}
  .pouch-art{position:absolute;inset:0}
  .reseal{position:absolute;right:10px;top:64px;font:600 11.5px "Exo 2",sans-serif;color:#fff;letter-spacing:.3px}
  .brand{position:absolute;left:0;right:0;top:176px;text-align:center;font:700 31px "Exo 2",sans-serif;color:var(--brand);letter-spacing:.5px}
  .headline{position:absolute;left:92px;font-style:italic;font-weight:900;line-height:1;
    background:linear-gradient(180deg,#ffffff 0%,#d9dadd 45%,#8f9096 55%,#e8e9ea 100%);
    -webkit-background-clip:text;background-clip:text;color:transparent}
  .headline--natural{top:220px;font-size:84px;letter-spacing:-1px}
  .headline--whey{top:284px;left:98px;font-size:126px;letter-spacing:-2px;
    background:linear-gradient(90deg,#ffffff 0%,#e8f0f2 40%,#7fd9e6 80%,#3cb8cc 100%);
    -webkit-background-clip:text;background-clip:text}
  .protein{position:absolute;left:168px;top:396px;font:300 42px "Exo 2",sans-serif;color:var(--pink);letter-spacing:1px}
  .claim{position:absolute;height:50px;padding:4px 22px 0 30px;color:var(--teal-text);line-height:1;
    background:linear-gradient(180deg,#ffffff 0%,#e4e5e7 50%,#b9babe 100%);
    border-radius:12px 22px 12px 22px;transform:skewX(-14deg)}
  .claim > span{display:block;transform:skewX(14deg)}
  .claim small{font:500 13px "Orbitron",sans-serif;color:#1f5259;display:block}
  .claim strong{font:700 25px "Orbitron",sans-serif}
  .claim em{font:500 12px "Orbitron",sans-serif;font-style:normal}
  .claim--flavours{left:137px;top:465px;width:222px}
  .claim--amino{left:183px;top:528px;width:310px}
  .claim--protein{left:232px;top:590px;width:290px}
  .claim--protein strong{font-size:22px}
  .claim--protein em{font-size:11.5px;color:#1f5259}
  .weight{position:absolute;left:104px;top:672px;width:118px;height:118px}
  .weight-value{position:absolute;left:0;right:0;top:36px;text-align:center;font:italic 900 34px "Exo 2",sans-serif;color:#fff}
  .flavour-tag{position:absolute;left:268px;top:716px;width:186px;height:52px;border-radius:14px;
    background:#111;border:3px solid var(--silver-mid);display:flex;align-items:center;gap:8px;padding-left:6px}
  .flavour-icon{width:40px;height:40px;border-radius:50%;background:#3a3a3e;border:2px solid var(--silver-mid);flex:none}
  .flavour-text{line-height:1}
  .flavour-text b{display:block;font:700 19px "Exo 2",sans-serif;color:#f3b3e3}
  .flavour-text i{display:block;font:600 13px "Exo 2",sans-serif;color:#ddd;font-style:normal;margin-left:30px}
</style>
</head>
<body>
<div class="canvas">
  <div class="pouch">
    <svg class="pouch-art" width="512" height="808" viewBox="0 0 512 808" xmlns="http://www.w3.org/2000/svg">
      <defs>
        <linearGradient id="silverTop" x1="0" y1="0" x2="0" y2="1">
          <stop offset="0" stop-color="#dcdde0"/><stop offset=".4" stop-color="#f4f4f6"/><stop offset="1" stop-color="#b6b7bb"/>
        </linearGradient>
        <linearGradient id="sideShade" x1="0" y1="0" x2="1" y2="0">
          <stop offset="0" stop-color="#000" stop-opacity=".0"/><stop offset=".5" stop-color="#000" stop-opacity="0"/><stop offset="1" stop-color="#000" stop-opacity=".35"/>
        </linearGradient>
        <linearGradient id="glow" x1="0" y1="0" x2="1" y2="0">
          <stop offset="0" stop-color="#c2376e" stop-opacity=".55"/><stop offset=".45" stop-color="#5b2a6e" stop-opacity=".35"/><stop offset="1" stop-color="#35c3d8" stop-opacity=".7"/>
        </linearGradient>
        <linearGradient id="fadeUp" x1="0" y1="0" x2="0" y2="1">
          <stop offset="0" stop-color="#000" stop-opacity=".9"/><stop offset=".35" stop-color="#000" stop-opacity=".2"/><stop offset="1" stop-color="#000" stop-opacity=".4"/>
        </linearGradient>
        <linearGradient id="swoosh" x1="0" y1="0" x2="1" y2="0">
          <stop offset="0" stop-color="#b0223f"/><stop offset=".5" stop-color="#2a1a2a"/><stop offset="1" stop-color="#36c8dc"/>
        </linearGradient>
        <linearGradient id="ring" x1="0" y1="0" x2="0" y2="1">
          <stop offset="0" stop-color="#fafafa"/><stop offset="1" stop-color="#8f9095"/>
        </linearGradient>
      </defs>
      <rect width="512" height="808" fill="var(--pouch-dark)"/>
      <g role="img" aria-label="Halftone dot pattern glowing pink to cyan">
        <rect x="0" y="170" width="512" height="638" fill="url(#glow)"/>
        <rect x="0" y="170" width="512" height="638" fill="url(#fadeUp)"/>
      </g>
      <path d="M0 150 C120 120 300 150 512 120 L512 175 C330 165 150 150 0 205 Z" fill="url(#swoosh)"/>
      <path d="M0 0 H512 V150 C330 160 170 120 0 175 Z" fill="url(#silverTop)"/>
      <path d="M0 10 H512" stroke="#fff" stroke-opacity=".6" stroke-width="2"/>
      <path d="M10 36 H450" stroke="#555" stroke-width="2" stroke-dasharray="18 12"/>
      <g stroke="#555" stroke-width="1.6" fill="none">
        <circle cx="470" cy="31" r="3.5"/><circle cx="470" cy="42" r="3.5"/>
        <path d="M473 33 L492 41 M473 40 L492 32"/>
      </g>
      <rect width="512" height="808" fill="url(#sideShade)"/>
      <rect x="0" y="0" width="14" height="808" fill="#000" opacity=".35"/>
    </svg>

    <p class="reseal">RESEAL AND KEEP FRESH</p>
    <p class="brand">STELLAR FUELWORKS</p>
    <p class="headline headline--natural">NATURAL</p>
    <p class="headline headline--whey">WHEY</p>
    <p class="protein">PROTEIN</p>

    <div class="claim claim--flavours"><span><small>NO ARTIFICIAL</small><strong>FLAVOURS</strong></span></div>
    <div class="claim claim--amino"><span><small>EXCELLENT</small><strong>AMINO ACID</strong><em> PROFILE</em></span></div>
    <div class="claim claim--protein"><span><strong>80% HIGH</strong><br><em>QUALITY PROTEIN CONTENT</em></span></div>

    <div class="weight">
      <svg width="118" height="118" viewBox="0 0 118 118" xmlns="http://www.w3.org/2000/svg">
        <defs>
          <path id="arcTop" d="M21 59 A38 38 0 0 1 97 59"/>
          <path id="arcBottom" d="M17 59 A42 42 0 0 0 101 59"/>
        </defs>
        <circle cx="59" cy="59" r="57" fill="url(#ring)"/>
        <circle cx="59" cy="59" r="50" fill="#fff" opacity=".85"/>
        <circle cx="59" cy="59" r="34" fill="#1a1a1f"/>
        <text font-family="Exo 2, sans-serif" font-weight="700" font-size="12" fill="#222"><textPath href="#arcTop" startOffset="50%" text-anchor="middle">30 servings</textPath></text>
        <text font-family="Exo 2, sans-serif" font-weight="700" font-size="12" fill="#222"><textPath href="#arcBottom" startOffset="50%" text-anchor="middle">30 servings</textPath></text>
        <text x="12" y="63" font-size="10" fill="#222">★</text>
        <text x="97" y="63" font-size="10" fill="#222">★</text>
      </svg>
      <p class="weight-value">909g</p>
    </div>

    <div class="flavour-tag">
      <span class="flavour-icon" role="img" aria-label="Strawberry icon"></span>
      <span class="flavour-text"><b>Strawberry</b><i>flavour</i></span>
    </div>
  </div>
</div>
</body>
</html>
```